Harlow Crest Holdings (Remodeling company) needs a logo and business card

We need a business card design for a new company. We "flip" upmarket houses (buy, remodel and sell) in the Austin, TX area. I'd like neutral colors (grey, white, gold black). I would like it to include a simple, clean logo. Our designs are modern and uncluttered and I would like that reflected in the business card design.

Target Market(s)

Young professionals, Families, Retirees. Our properties will sell for $750k+

Industry/Entity Type

Real Estate

Contact Information for Business Card

Harlow Crets Holdings
Mona Harlow
(979) 555 0142
Owner
Rolf Tandem
(512) 555 0176
Realtor

Logo Text

Harlow Crest Holdings

Font styles to use
Serif
Script

Requirements
Must have
• Simple, classic design
Nice to have
• Clean lines, modern look
Should not have
• Too traditionally

```html
<!DOCTYPE html>
<html lang="en">
<head>
<meta charset="utf-8">
<title>Harlow Crest Holdings – Business Card</title>
<link rel="stylesheet" href="https://fonts.googleapis.com/css2?family=Cinzel:wght@500&family=Source+Sans+3:wght@600&family=Crimson+Text:wght@600&display=swap">
<style>
  :root {
    --card-black: #121212;
    --gold: #e9cb22;
    --gold-line: #d8bb1e;
  }
  * { margin: 0; padding: 0; box-sizing: border-box; }
  html, body {
    width: 1200px;
    height: 780px;
    overflow: hidden;
    background: var(--card-black);
  }
  .card {
    position: relative;
    width: 1200px;
    height: 780px;
    background: var(--card-black);
    color: var(--gold);
  }
  .brand {
    position: absolute;
    top: 150px;
    left: 0;
    width: 1200px;
    text-align: center;
    font-family: "Cinzel", "Times New Roman", serif;
    font-weight: 500;
    font-size: 62px;
    letter-spacing: 4px;
    text-transform: uppercase;
  }
  .brand-rule {
    position: absolute;
    top: 272px;
    left: 240px;
    width: 720px;
    height: 2px;
    background: var(--gold-line);
  }
  .column-divider {
    position: absolute;
    top: 370px;
    left: 599px;
    width: 2px;
    height: 200px;
    background: var(--gold-line);
  }
  .contact {
    position: absolute;
    top: 360px;
    width: 440px;
  }
  .contact--owner { left: 120px; text-align: right; }
  .contact--realtor { left: 640px; text-align: left; }
  .contact-name {
    font-family: "Source Sans 3", "Helvetica Neue", sans-serif;
    font-weight: 600;
    font-size: 60px;
    line-height: 1;
  }
  .contact-role {
    font-family: "Source Sans 3", "Helvetica Neue", sans-serif;
    font-weight: 600;
    font-size: 34px;
    line-height: 1.2;
  }
  .contact--owner .contact-role { padding-right: 4px; }
  .contact--realtor .contact-role { padding-left: 48px; }
  .contact-phone {
    display: flex;
    align-items: center;
    gap: 16px;
    margin-top: 40px;
    font-family: "Crimson Text", "Times New Roman", serif;
    font-weight: 600;
    font-size: 40px;
  }
  .contact--owner .contact-phone { justify-content: flex-end; }
  .phone-icon { width: 38px; height: 38px; flex: none; }
</style>
</head>
<body>
  <div class="card">
    <div class="brand">Harlow Crets Holdings</div>
    <div class="brand-rule"></div>

    <div class="contact contact--owner">
      <div class="contact-name">Mona Harlow</div>
      <div class="contact-role">Owner</div>
      <div class="contact-phone">
        <svg class="phone-icon" viewBox="0 0 38 38" aria-hidden="true">
          <rect width="38" height="38" fill="var(--gold)"/>
          <path d="M10 15c0-4 4-6 9-6s9 2 9 6l-4 1-1-3h-8l-1 3z M12 18h14l2 10H10z" fill="var(--card-black)"/>
          <circle cx="19" cy="23" r="3" fill="var(--gold)"/>
        </svg>
        <span>(979) 555 0142</span>
      </div>
    </div>

    <div class="column-divider"></div>

    <div class="contact contact--realtor">
      <div class="contact-name">Rolf Tandem</div>
      <div class="contact-role">Realtor</div>
      <div class="contact-phone">
        <svg class="phone-icon" viewBox="0 0 38 38" aria-hidden="true">
          <rect width="38" height="38" fill="var(--gold)"/>
          <path d="M10 15c0-4 4-6 9-6s9 2 9 6l-4 1-1-3h-8l-1 3z M12 18h14l2 10H10z" fill="var(--card-black)"/>
          <circle cx="19" cy="23" r="3" fill="var(--gold)"/>
        </svg>
        <span>(512) 555 0176</span>
      </div>
    </div>
  </div>
</body>
</html>
```